Black Car Limousine transportation business in Naples Florida

Brightway stand for my reliability and DPR stands for Devotion, P and R are the first initials of my children's names. It should show professionalism and a dedication to customer service. We keep our clients identities private. Show our professionalism. We are Black car Black tie company. We service transportation on a reserve basis to and from residents, airports, casinos, hotels,

Target Market(s)

It is a Private car service. High end clients. Businesses, Celebrity and athletes. Service to airports, hotels, special events.

Industry/Entity Type

Business

Contact Information for Business Card

A pearl metallic or Luster card. Standard business card size. Would like the name, Company email, show we take credit cards and phone number. Currently I don't have a website but will like to add later.

Logo Text

BRIGHTWAY DPR TRANSPORTATION

Font styles to use
Serif

Colors
eaeaea
000000

Requirements
Must have
• Must have Company email, show we take credit cards and phone number. Currently I don't have a website but will like to add later.
Nice to have
• Would like to stay with a black and white theme. Open to some color trim.
Should not have
• Open to suggestions

```html
<!DOCTYPE html>
<html lang="en">
<head>
<meta charset="UTF-8">
<title>Brightway DPR Transportation – Business Card</title>
<link rel="stylesheet" href="https://fonts.googleapis.com/css2?family=Cormorant+Garamond:wght@600&family=Open+Sans:wght@400;700&display=swap">
<style>
  :root {
    --backdrop: #3a322d;
    --card: #0b0b0b;
    --card-edge: #1a1a1a;
    --ink-light: #eaeaea;
    --ink-mid: #bdbdbd;
    --divider: #5a5a5a;
  }
  * { margin: 0; padding: 0; box-sizing: border-box; }
  html, body {
    width: 1200px;
    height: 900px;
    overflow: hidden;
    background: var(--backdrop);
    font-family: "Open Sans", Arial, sans-serif;
  }
  .stage { position: relative; width: 1200px; height: 900px; }

  .card {
    position: absolute;
    top: 302px;
    width: 520px;
    height: 297px;
    background: var(--card);
    border: 1px solid var(--card-edge);
    box-shadow: 0 10px 30px rgba(0,0,0,0.45);
  }
  .card--front { left: 50px; }
  .card--back { left: 630px; }

  .wordmark {
    font-family: "Cormorant Garamond", Georgia, serif;
    color: var(--ink-light);
    font-weight: 600;
    text-transform: uppercase;
    line-height: 1.1;
  }
  .wordmark__line { display: block; }

  .card--front .wordmark {
    position: absolute;
    left: 38px;
    top: 118px;
    width: 200px;
    font-size: 23px;
    letter-spacing: 0.6px;
  }

  .card__divider {
    position: absolute;
    left: 252px;
    top: 95px;
    width: 1px;
    height: 118px;
    background: var(--divider);
  }

  .contact {
    position: absolute;
    left: 272px;
    top: 104px;
    color: var(--ink-light);
  }
  .contact__name {
    font-size: 19px;
    font-weight: 700;
    margin-bottom: 12px;
  }
  .contact__row {
    display: flex;
    align-items: center;
    gap: 8px;
    font-size: 11.5px;
    color: var(--ink-mid);
    margin-bottom: 6px;
    white-space: nowrap;
  }
  .contact__row svg { flex: none; fill: var(--ink-mid); }

  .card--back .wordmark {
    position: absolute;
    left: 0;
    right: 0;
    top: 114px;
    text-align: center;
    font-size: 28px;
    letter-spacing: 1.2px;
  }
</style>
</head>
<body>
<main class="stage">
  <section class="card card--front" aria-label="Business card front">
    <div class="wordmark">
      <span class="wordmark__line">Brightway DPR</span>
      <span class="wordmark__line">Transportation</span>
    </div>
    <div class="card__divider"></div>
    <div class="contact">
      <p class="contact__name">Daniel Moretti</p>
      <p class="contact__row">
        <svg width="11" height="11" viewBox="0 0 24 24" aria-hidden="true"><path d="M6.6 10.8a15.1 15.1 0 0 0 6.6 6.6l2.2-2.2a1 1 0 0 1 1-.25 11.4 11.4 0 0 0 3.6.57 1 1 0 0 1 1 1V20a1 1 0 0 1-1 1A17 17 0 0 1 3 4a1 1 0 0 1 1-1h3.5a1 1 0 0 1 1 1c0 1.25.2 2.45.57 3.57a1 1 0 0 1-.25 1z"/></svg>
        <span>877-555-0142</span>
      </p>
      <p class="contact__row">
        <svg width="11" height="9" viewBox="0 0 24 18" aria-hidden="true"><path d="M0 0h24v18H0z M2 2v1l10 7 10-7V2z" fill-rule="evenodd"/></svg>
        <span>brightwaydprtransportation@mail.com</span>
      </p>
      <p class="contact__row">
        <svg width="12" height="9" viewBox="0 0 24 18" aria-hidden="true"><path d="M2 0h20a2 2 0 0 1 2 2v14a2 2 0 0 1-2 2H2a2 2 0 0 1-2-2V2a2 2 0 0 1 2-2z M0 4v3h24V4z M3 12v2h6v-2z" fill-rule="evenodd"/></svg>
        <span>Major credit cards accepted</span>
      </p>
    </div>
  </section>

  <section class="card card--back" aria-label="Business card back">
    <div class="wordmark">
      <span class="wordmark__line">Brightway DPR</span>
      <span class="wordmark__line">Transportation</span>
    </div>
  </section>
</main>
</body>
</html>
```